Corporate Brightfen business cards to be handed to investor, bankers etc. Needs to have a young feel

I need business cards designed for a technology company that provides uber-like rapid response on the security industry. I would like it simple but very cool and tasteful. See attached documents for artwork and colours to be used. Cut sheet describes business model. Card stock should be thicker than normal. I would like the one side to be just the art and the other to have the contact info with maybe the pin somewhere.

Target Market(s)

Investors

Industry/Entity Type

Business

Contact Information for Business Card

Would like the logo attached on one side with name address and other info on the other side.

Font styles to use
Other font styles liked:
• See existing logo

Colors
6b449b
886aae
e4daeb
ffffff

Requirements
Must have
• Name: Dorian Felkatsis
• Address: 47 Larkfield Avenue, Toronto, On, M6K2B7
• Tel: 416-7291846
• Email: rolo@brightfen.io
Nice to have
• See logo colours

```html
<!DOCTYPE html>
<html lang="en">
<head>
<meta charset="utf-8">
<title>Brightfen Business Card</title>
<link href="https://fonts.googleapis.com/css2?family=Lato:wght@300;400;700&display=swap" rel="stylesheet">
<style>
  :root {
    --purple-deep: #6b449b;
    --purple-mid: #7d5ca3;
    --purple-soft: #886aae;
    --lilac: #e4daeb;
    --white: #ffffff;
    --ink: #1f1c22;
    --backdrop: #e9e6ec;
  }
  * { box-sizing: border-box; margin: 0; padding: 0; }
  html, body {
    width: 1200px; height: 900px; overflow: hidden;
    background: var(--backdrop);
    font-family: "Lato", Arial, sans-serif;
  }
  .canvas {
    width: 1200px; height: 900px;
    display: flex; flex-direction: column;
    align-items: center; justify-content: center; gap: 60px;
  }
  .card {
    width: 630px; height: 360px;
    position: relative; overflow: hidden;
    box-shadow: 0 6px 18px rgba(40, 20, 60, 0.18);
  }

  /* Front: contact side */
  .card-front { background: var(--white); }
  .card-front .edge-band {
    position: absolute; left: 0; right: 0; bottom: 0;
    height: 10px; background: var(--purple-mid);
  }
  .front-wordmark {
    position: absolute; left: 48px; top: 98px;
    display: flex; align-items: center; gap: 8px;
  }
  .front-wordmark .dot {
    width: 16px; height: 16px; border-radius: 50%;
    background: var(--purple-mid);
  }
  .front-wordmark .name {
    font-weight: 300; font-size: 50px; letter-spacing: -0.5px;
    color: var(--ink); line-height: 1;
  }
  .divider {
    position: absolute; left: 340px; top: 112px;
    width: 2px; height: 180px; background: var(--purple-soft);
  }
  .contact {
    position: absolute; left: 362px; top: 112px;
    color: var(--ink); font-size: 17px; line-height: 1.35;
  }
  .contact .person {
    color: var(--purple-mid); font-size: 24px; font-weight: 400;
    margin-bottom: 8px; white-space: nowrap;
  }
  .contact .line { display: flex; align-items: center; gap: 8px; white-space: nowrap; }
  .contact .line svg { width: 13px; height: 13px; flex: none; fill: var(--purple-mid); }
  .contact .plain { padding-left: 21px; }

  /* Back: art side */
  .card-back { background: var(--purple-mid); }
  .back-wordmark {
    position: absolute; left: 240px; top: 140px;
    font-weight: 300; font-size: 78px; letter-spacing: -1px;
    color: var(--white); line-height: 1;
  }
</style>
</head>
<body>
<main class="canvas">
  <section class="card card-front" aria-label="Business card, contact side">
    <div class="front-wordmark">
      <span class="dot"></span>
      <span class="name">brightfen</span>
    </div>
    <div class="divider"></div>
    <div class="contact">
      <p class="person">Dorian Felkatsis</p>
      <p class="plain">47 Larkfield Avenue</p>
      <p class="plain">Toronto, On, M6K2B7</p>
      <p class="line">
        <svg viewBox="0 0 24 24" aria-hidden="true"><path d="M6.6 10.8a15.1 15.1 0 0 0 6.6 6.6l2.2-2.2c.3-.3.7-.4 1-.2 1.1.4 2.3.6 3.6.6.6 0 1 .4 1 1V20c0 .6-.4 1-1 1A17 17 0 0 1 3 4c0-.6.4-1 1-1h3.5c.6 0 1 .4 1 1 0 1.3.2 2.5.6 3.6.1.3 0 .7-.2 1z"/></svg>
        416-7291846
      </p>
      <p class="line">
        <svg viewBox="0 0 24 24" aria-hidden="true"><path d="M2 5h20v14H2z M2 5l10 8 10-8" fill="none" stroke="#7d5ca3" stroke-width="2"/></svg>
        rolo@brightfen.io
      </p>
    </div>
    <div class="edge-band"></div>
  </section>

  <section class="card card-back" aria-label="Business card, brand side">
    <span class="back-wordmark">brightfen</span>
  </section>
</main>
</body>
</html>
```